Patternmaking service (fashion) card design

I need cards for my patternmaking service. I service both large and small fashion labels including ladies,mens and childrenswear. I would like cards that have a sort of vintage feel, especially 50's and 60's style. Pink is my signature colour. Its important to have a fashion reference of some kind.

Industry/Entity Type

Fashion

Contact Information for Business Card

Marigold Lantern, Patternmaking Service, Pennae Falcastro,
27 Wexbury Lane. Ashvale Ridge. WKT. 4921. 0415836204, email:spoolinda4@quillmail.example. "By appointment only"

```html
<!DOCTYPE html>
<html lang="en">
<head>
<meta charset="utf-8">
<title>Marigold Lantern – Business Card</title>
<link rel="stylesheet" href="https://fonts.googleapis.com/css2?family=Playball&family=Arvo:wght@700&family=Josefin+Sans:wght@300&display=swap">
<style>
  :root {
    --backdrop: #2a2a2a;
    --card: #ffffff;
    --card-shade: #f2f2f2;
    --card-edge: #e6e6e6;
    --signature-pink: #c2188f;
    --ink: #3a3a3a;
    --ink-soft: #6e6e6e;
    --ornament-dark: #4a4a4a;
    --ornament-mid: #8a8a8a;
    --ornament-light: #cfcfcf;
  }
  html, body {
    margin: 0;
    padding: 0;
    width: 1200px;
    height: 993px;
    overflow: hidden;
    background: var(--backdrop);
  }
  .canvas {
    position: relative;
    width: 1200px;
    height: 993px;
  }
  .business-card {
    position: absolute;
    left: 100px;
    top: 210px;
    width: 1000px;
    height: 572px;
    background: linear-gradient(180deg, var(--card) 0%, var(--card-shade) 100%);
    border: 1px solid var(--card-edge);
    box-sizing: border-box;
    text-align: center;
  }
  .ornament-band {
    position: absolute;
    left: 70px;
    right: 70px;
    height: 80px;
    border-radius: 40px;
    background: radial-gradient(ellipse at center, var(--ornament-dark) 0%, var(--ornament-mid) 45%, var(--ornament-light) 80%, rgba(255,255,255,0) 100%);
    opacity: 0.5;
  }
  .ornament-band--top { top: 52px; }
  .ornament-band--bottom { top: 462px; }
  .brand-name {
    position: absolute;
    left: 0; right: 0;
    top: 140px;
    margin: 0;
    font-family: 'Playball', cursive;
    font-weight: 400;
    font-size: 56px;
    line-height: 64px;
    color: var(--signature-pink);
  }
  .brand-service {
    position: absolute;
    left: 0; right: 0;
    top: 212px;
    margin: 0;
    font-family: 'Josefin Sans', sans-serif;
    font-weight: 300;
    font-size: 22px;
    line-height: 26px;
    letter-spacing: 8px;
    color: var(--ink-soft);
  }
  .person {
    position: absolute;
    left: 0; right: 0;
    top: 256px;
    font-family: 'Arvo', serif;
    font-weight: 700;
    font-size: 23px;
    line-height: 31px;
    color: var(--ink);
  }
  .contact {
    position: absolute;
    left: 0; right: 0;
    top: 338px;
    font-family: 'Josefin Sans', sans-serif;
    font-weight: 300;
    font-size: 20px;
    line-height: 34px;
    color: var(--ink-soft);
  }
  .contact p, .person p { margin: 0; }
</style>
</head>
<body>
  <main class="canvas">
    <section class="business-card">
      <div class="ornament-band ornament-band--top" role="img" aria-label="Engraved baroque acanthus scroll ornament, black and grey"></div>
      <div class="ornament-band ornament-band--bottom" role="img" aria-label="Engraved baroque acanthus scroll ornament, black and grey"></div>

      <h1 class="brand-name">Marigold Lantern</h1>
      <p class="brand-service">patternmakingservice</p>

      <div class="person">
        <p class="person-name">Dorian Wexley</p>
        <p class="person-role">Managing Director</p>
      </div>

      <div class="contact">
        <p class="contact-address">Pennae Falcastro. 27 Wexbury Lane. Ashvale Ridge. WKT</p>
        <p class="contact-email">spoolinda4@quillmail.example. "By appointment only"</p>
        <p class="contact-phone">4921. 0415836204</p>
      </div>
    </section>
  </main>
</body>
</html>
```